Wordpress Design for a Digital Management Consulting Business

I need a simple Wordpress Design and someone to set it up for a new boutique management consulting business called Tidewell Advisory that specialises in providing strategic advice to help grow digital businesses. It covers business strategy, marketing strategy, digital strategy, web product development, marketing campaigns, social, search, etc. From strategy to implementation.

URL is: tidewelladvisory.com.au

My professional background is here: au.examplenet.com/in/norabellweather

Competitors: other boutique digital/marketing management consulting businesses in Australia

The logos, colours and fonts are attached.

I would like the site to convey a business that is Smart/intelligent, Contemporary, Progressive, Digital, Energetic, Friendly.

The objective of the site is to educate visitors about what Tidewell Advisory does and encourage them to contact me for more information. It will be very light on content.

Target Market(s)

CEOs/Managing Directors, General Managers, Marketing Directors

Industry/Entity Type

Management Consulting

Font styles to use
Sans Serif

Colors
e34197
5c5c5c
000000

Requirements
Must have
• Site design requirements:
• Choose an appropriate Wordpress template, set it up for me and let me be able to edit it ongoing.
• It should use lots of images - these can be inspirational and not necessarily tied directly to the work
• Pink should feature, but not be the dominant colour.
• Site structure should be:
• 1. Home page - image led with horizontal navigation. Text beneath and images to describe the services.
• 2. About page - with space to write text and insert a picture of the Director
• 3. Services - with space to highlight services either as a list or graphically with text
• 4. Contact page - with space to write text and add email links, etc.
• Should have horizontal navigation
• It should have the flexibility to add another page
Nice to have
• Use the tree icon somehow in the design - consider in the background enlarged
• Use pink, grey, black from logo. Can introduce another complimentary colour if necessary.
• Can introduce another complimentary font to go with the logo font.
Should not have
• Use cliched business images and icons, eg. business suits, hand shakes, business men, business ties.

```html
<!DOCTYPE html>
<html lang="en">
<head>
<meta charset="utf-8">
<title>Tidewell Advisory – Marketing Strategy &amp; Consulting</title>
<link href="https://fonts.googleapis.com/css2?family=Raleway:wght@400;500;600;700&display=swap" rel="stylesheet">
<style>
:root{
  --pink:#e34197;
  --grey:#5c5c5c;
  --black:#000000;
  --light:#f2f2f2;
  --white:#ffffff;
  --board:#23292e;
  --board-mid:#3b454c;
  --frame-blue:#3f6f9a;
  --desk:#e9e6e1;
}
*{box-sizing:border-box;margin:0;padding:0}
html,body{width:795px;height:1200px;overflow:hidden}
body{font-family:'Raleway',sans-serif;color:var(--grey);background:var(--white);position:relative}
.container{width:505px;margin:0 auto;position:relative}

/* header */
.site-header{height:36px;background:var(--white);position:relative}
.site-header .container{display:flex;align-items:center;justify-content:space-between;height:36px}
.brand{display:flex;align-items:center;gap:6px;color:var(--pink);font-weight:600;line-height:1}
.brand-dot{width:18px;height:18px;border-radius:50%;background:var(--pink)}
.brand-name{display:flex;flex-direction:column}
.brand-name .main{font-size:15px;letter-spacing:1px}
.brand-name .sub{font-size:6.5px;letter-spacing:2.6px;margin-top:2px}
.main-nav{display:flex;gap:17px;font-size:6.5px;font-weight:600;letter-spacing:.5px;color:var(--grey)}
.main-nav a{color:inherit;text-decoration:none;padding:4px 0}
.main-nav a.active{color:var(--pink);border-bottom:1px solid var(--pink)}

/* hero */
.hero{height:336px;position:relative;color:var(--white);text-align:center;overflow:hidden}
.hero-media{position:absolute;inset:0;background:
  radial-gradient(ellipse 140px 60px at 47% 30%,rgba(227,65,151,.55),rgba(227,65,151,0) 100%),
  radial-gradient(ellipse 260px 70px at 60% 22%,rgba(255,255,255,.16),rgba(255,255,255,0) 100%),
  radial-gradient(ellipse 220px 60px at 28% 62%,rgba(255,255,255,.12),rgba(255,255,255,0) 100%),
  radial-gradient(ellipse 180px 140px at 97% 4%,var(--desk) 0%,rgba(233,230,225,.6) 45%,rgba(233,230,225,0) 80%),
  radial-gradient(ellipse 160px 120px at 100% 100%,rgba(120,95,70,.75),rgba(120,95,70,0) 100%),
  linear-gradient(100deg,var(--frame-blue) 0%,#2c4a66 6%,var(--board) 14%,var(--board-mid) 50%,var(--board) 82%,#4b3b2e 100%)}
.hero-shade{position:absolute;inset:0;background:linear-gradient(180deg,rgba(0,0,0,0) 35%,rgba(0,0,0,.35) 60%,rgba(0,0,0,.1) 100%)}
.hero-content{position:absolute;left:0;right:0;top:150px}
.hero-title{font-size:23px;font-weight:700;letter-spacing:.3px}
.hero-sub{font-size:11px;font-weight:600;color:var(--pink);letter-spacing:1px;margin-top:4px}
.btn{display:inline-block;font-family:'Raleway',sans-serif;font-size:5.5px;font-weight:600;letter-spacing:.6px;text-decoration:none}
.btn-ghost{border:1px solid var(--white);color:var(--white);padding:4px 10px;margin-top:14px}
.slider-dots{position:absolute;left:0;right:0;bottom:22px;display:flex;justify-content:center;gap:4px}
.slider-dots span{width:5px;height:5px;border-radius:50%;background:rgba(255,255,255,.55)}
.slider-dots span.on{background:var(--white)}

/* welcome */
.welcome{background:var(--light);height:176px;text-align:center;padding-top:28px}
.welcome h1{font-size:17px;font-weight:500;color:#333;letter-spacing:.3px}
.rule{width:60px;height:1px;background:var(--pink);margin:6px auto 8px}
.welcome .lead{font-size:6px;font-weight:700;color:#444;margin-bottom:6px}
.welcome p{font-size:5.5px;line-height:1.6;width:470px;margin:0 auto 5px}

/* services */
.services{padding-top:32px}
.service-grid{display:grid;grid-template-columns:repeat(3,1fr);column-gap:18px;row-gap:22px}
.service{text-align:center}
.service-media{height:78px;width:100%}
.service h2{font-size:7px;font-weight:700;color:#333;letter-spacing:.4px;margin-top:16px;line-height:1.3}
.service p{font-size:5.5px;line-height:1.55;width:120px;margin:4px auto 0}
.btn-outline{border:1px solid var(--pink);color:var(--pink);padding:3px 9px;margin-top:7px}
.m1{background:
  radial-gradient(ellipse 50px 25px at 55% 45%,rgba(70,90,110,.35),rgba(70,90,110,0)),
  radial-gradient(ellipse 40px 20px at 25% 70%,rgba(80,80,80,.25),rgba(80,80,80,0)),
  linear-gradient(160deg,#f4f4f2,#d9dcdf 60%,#aeb5bb)}
.m2{background:
  radial-gradient(ellipse 40px 22px at 55% 40%,rgba(227,65,151,.75),rgba(227,65,151,0)),
  radial-gradient(ellipse 45px 25px at 25% 65%,rgba(90,200,230,.55),rgba(90,200,230,0)),
  radial-gradient(ellipse 35px 20px at 80% 75%,rgba(240,190,60,.5),rgba(240,190,60,0)),
  linear-gradient(135deg,#1e2a3a,#3a4f66)}
.m3{background:
  radial-gradient(ellipse 30px 16px at 30% 35%,rgba(227,65,151,.45),rgba(227,65,151,0)),
  radial-gradient(ellipse 34px 18px at 70% 65%,rgba(92,92,92,.35),rgba(92,92,92,0)),
  linear-gradient(135deg,#eceeef,#d2d5d8)}
.m4{background:
  radial-gradient(ellipse 35px 20px at 30% 35%,rgba(255,170,60,.7),rgba(255,170,60,0)),
  radial-gradient(ellipse 35px 20px at 70% 60%,rgba(120,210,120,.6),rgba(120,210,120,0)),
  radial-gradient(ellipse 30px 18px at 50% 80%,rgba(227,65,151,.55),rgba(227,65,151,0)),
  linear-gradient(135deg,#5f8fc4,#2e5684)}
.m5{background:
  radial-gradient(ellipse 30px 20px at 25% 30%,rgba(240,80,60,.7),rgba(240,80,60,0)),
  radial-gradient(ellipse 30px 20px at 70% 30%,rgba(60,160,230,.75),rgba(60,160,230,0)),
  radial-gradient(ellipse 35px 20px at 45% 75%,rgba(250,200,50,.7),rgba(250,200,50,0)),
  radial-gradient(ellipse 30px 18px at 85% 80%,rgba(80,190,110,.6),rgba(80,190,110,0)),
  linear-gradient(135deg,#3e5d86,#2a2f45)}
.m6{background:
  radial-gradient(circle 22px at 30% 45%,rgba(235,235,235,.8),rgba(235,235,235,0)),
  radial-gradient(circle 20px at 70% 55%,rgba(220,220,220,.7),rgba(220,220,220,0)),
  linear-gradient(135deg,#1f1f1f,#555)}

/* newsletter */
.newsletter{position:absolute;top:975px;left:0;right:0;height:160px;background:linear-gradient(90deg,#e0378f,var(--pink) 50%,#d8378c);text-align:center;color:var(--white);padding-top:25px}
.newsletter h2{font-size:18px;font-weight:500;letter-spacing:.5px}
.newsletter p{font-size:5.5px;line-height:1.6;width:300px;margin:8px auto 0;opacity:.95}
.signup{display:flex;justify-content:center;margin-top:14px}
.signup .field{width:140px;height:16px;background:var(--white);color:#999;font-size:5px;text-align:left;padding:5px 6px}
.signup .submit{height:16px;background:#2b2b2b;color:var(--white);font-size:5px;font-weight:600;letter-spacing:.5px;padding:5px 8px}

/* footer */
.site-footer{position:absolute;top:1135px;left:0;right:0;height:65px;background:var(--black);color:#cfcfcf}
.site-footer .container{padding-top:18px}
.footer-row{display:flex;justify-content:space-between;align-items:center}
.footer-nav{font-size:6.5px;font-weight:600;color:var(--white)}
.footer-nav span{margin:0 4px;color:#888}
.social{display:flex;gap:5px}
.social span{width:8px;height:8px;border-radius:50%;background:var(--white)}
.copyright{font-size:4.5px;margin-top:6px;color:#999}
</style>
</head>
<body>

<header class="site-header">
  <div class="container">
    <div class="brand">
      <div class="brand-dot"></div>
      <div class="brand-name"><span class="main">TIDEWELL</span><span class="sub">ADVISORY</span></div>
    </div>
    <nav class="main-nav">
      <a class="active" href="#">HOME</a>
      <a href="#">ABOUT</a>
      <a href="#">SERVICES</a>
      <a href="#">CLIENTS</a>
      <a href="#">CONTACT</a>
    </nav>
  </div>
</header>

<section class="hero">
  <div class="hero-media" role="img" aria-label="Photo of a chalkboard with hand-written marketing and strategy words on a desk"></div>
  <div class="hero-shade"></div>
  <div class="hero-content">
    <div class="hero-title">MARKETING STRATEGY &amp; CONSULTING</div>
    <div class="hero-sub">FROM STRATEGY TO IMPLEMENTATION</div>
    <a class="btn btn-ghost" href="#">LEARN MORE</a>
  </div>
  <div class="slider-dots"><span class="on"></span><span></span><span></span><span></span></div>
</section>

<section class="welcome">
  <h1>WELCOME TO OUR WEBSITE MAINPAGE</h1>
  <div class="rule"></div>
  <div class="lead">Smart, contemporary advice that helps digital businesses grow with clarity and confidence.</div>
  <p>We partner with chief executives, managing directors and marketing leaders to shape strategy, sharpen digital channels and turn plans into measurable growth. Every engagement is tailored, practical and focused on outcomes that matter to your business.</p>
  <p>From strategy to implementation, we stay close to your team until the work is delivered.</p>
</section>

<section class="services">
  <div class="container service-grid">
    <article class="service">
      <div class="service-media m1" role="img" aria-label="Photo of a marketing strategy sketch on paper"></div>
      <h2>MARKETING STRATEGY</h2>
      <p>Clear plans that connect your brand, audience and channels to growth.</p>
      <a class="btn btn-outline" href="#">READ MORE</a>
    </article>
    <article class="service">
      <div class="service-media m2" role="img" aria-label="Photo of glowing digital devices and data"></div>
      <h2>DIGITAL STRATEGY</h2>
      <p>A roadmap for platforms, data and tools that move your business forward.</p>
      <a class="btn btn-outline" href="#">READ MORE</a>
    </article>
    <article class="service">
      <div class="service-media m3" role="img" aria-label="Photo of web product wireframes"></div>
      <h2>WEB PRODUCT<br>DEVELOPMENT</h2>
      <p>Useful digital products shaped around real customer needs.</p>
      <a class="btn btn-outline" href="#">READ MORE</a>
    </article>
    <article class="service">
      <div class="service-media m4" role="img" aria-label="Photo of a colourful campaign planning board"></div>
      <h2>MARKETING CAMPAIGNS</h2>
      <p>Campaigns built to reach the right people with the right message.</p>
      <a class="btn btn-outline" href="#">READ MORE</a>
    </article>
    <article class="service">
      <div class="service-media m5" role="img" aria-label="Colourful collage of social media and search imagery"></div>
      <h2>SOCIAL &amp; SEARCH</h2>
      <p>Visibility across social and search that keeps your brand front of mind.</p>
      <a class="btn btn-outline" href="#">READ MORE</a>
    </article>
    <article class="service">
      <div class="service-media m6" role="img" aria-label="Photo of interlocking metal gears"></div>
      <h2>IMPLEMENTATION</h2>
      <p>Hands-on support to turn strategy into delivered, measurable results.</p>
      <a class="btn btn-outline" href="#">READ MORE</a>
    </article>
  </div>
</section>

<section class="newsletter">
  <h2>NEWSLETTER SIGN UP</h2>
  <p>Join our mailing list for occasional insights on digital strategy, marketing and growth for ambitious businesses.</p>
  <div class="signup">
    <div class="field">Enter email address</div>
    <div class="submit">SUBSCRIBE</div>
  </div>
</section>

<footer class="site-footer">
  <div class="container">
    <div class="footer-row">
      <div class="footer-nav">Home<span>|</span>About Us<span>|</span>Blogs<span>|</span>Services<span>|</span>Contact</div>
      <div class="social"><span></span><span></span><span></span><span></span></div>
    </div>
    <div class="copyright">© 2024 Tidewell Advisory. All rights reserved. Terms of Use</div>
  </div>
</footer>

</body>
</html>
```